2 Wine Label Designs

Amberly Cellars has been helping people give customized wine gifts since 1999. From large scale corporate clients, to 1 bottle personalized gifts, we offer a wide range of wines and templates for any occasion. Recently we’ve started to shift our focus to a younger demographic (21 to 35 year old women) and are in the process of updating our website and branding.

One big area we’re working to improve is the customizable wine label/engraving templates we offer on the site (to see our current template library go to www.amberlycellars.com/shop/wine, select a wine, choose “label” or “engraving” from the dropdown, and click “customize”). You’ll find that a lot of our current templates are outdated or aimed at an older demographic. Over the next few months we want to swap out most of these old templates with fun fresh designs.

We're asking designers to submit 2 customizable wine label templates for this project. One should be wedding themed and the other "Thank You" themed. Please see the attached PDF for more guidelines and creative direction.

Keep in mind, even if you aren't selected as the winner of this project we are going to go through and offer $50 for any label template submitted that we like ($100 if we want both). So there is a good chance you'll be getting some money for your work!

Please read though the attached guidelines PDF carefully (especially the "Must be Customizable" section).

Target Market(s)

21 to 35 year old women

Colors

Designer to choose colors to be used in the design.

Requirements
Must have
• See attached PDF
Nice to have
• See attached PDF
Should not have
• See attached PDF

```html
<!DOCTYPE html>
<html lang="en">
<head>
<meta charset="utf-8">
<title>Wedding Wine Label – Amberly Cellars Template</title>
<link rel="stylesheet" href="https://fonts.googleapis.com/css2?family=Comfortaa:wght@500;700&family=Playfair+Display:ital,wght@0,800;1,500;1,700&family=Montserrat:wght@600&display=swap">
<style>
  :root{
    --page:#d9d4d1;
    --label-base:#c9d8dc;
    --label-light:#e6e8ea;
    --petal:#f2a9a3;
    --petal-soft:#f7cfc8;
    --core:#262f42;
    --ink:#2c3448;
    --white:#ffffff;
  }
  *{box-sizing:border-box;margin:0;padding:0}
  html,body{width:1200px;height:1200px;overflow:hidden;background:var(--page)}
  .canvas{position:relative;width:1200px;height:1200px;display:flex;align-items:center;justify-content:center}
  .label{
    position:relative;width:780px;height:1060px;overflow:hidden;
    background:linear-gradient(180deg,var(--label-light) 0%,var(--label-base) 70%,#bfd0d6 100%);
    box-shadow:0 14px 40px rgba(40,40,50,.18);
  }
  .floral-art{position:absolute;left:0;top:0;width:780px;height:1060px}
  .label-content{position:relative;z-index:1;height:100%;display:flex;flex-direction:column;align-items:center;padding-top:78px;color:var(--ink);text-align:center}
  .invite-line{font-family:"Comfortaa",sans-serif;font-weight:700;font-size:27px;letter-spacing:.16em;text-transform:uppercase}
  .rule{width:520px;height:2px;background:var(--ink);margin-top:14px}
  .rule.short{width:200px;margin-top:10px}
  .event-title{font-family:"Playfair Display",serif;font-style:italic;font-weight:500;font-size:118px;line-height:1;margin-top:34px}
  .couple{margin-top:40px;display:flex;align-items:flex-start;justify-content:center;gap:14px;color:var(--white)}
  .partner{display:flex;flex-direction:column;align-items:center}
  .first-name{font-family:"Playfair Display",serif;font-weight:800;font-size:108px;line-height:1}
  .surname{font-family:"Montserrat",sans-serif;font-weight:600;font-size:28px;letter-spacing:.08em;text-transform:uppercase;margin-top:6px}
  .amp{font-family:"Playfair Display",serif;font-style:italic;font-weight:700;font-size:66px;line-height:1;margin-top:34px}
  .details{margin-top:60px;font-family:"Comfortaa",sans-serif;font-weight:700;font-size:30px;letter-spacing:.14em;text-transform:uppercase;line-height:1.45}
  .details sup{font-size:.5em;letter-spacing:.05em}
  .venue-heading{margin-top:58px;font-family:"Comfortaa",sans-serif;font-weight:700;font-size:27px;letter-spacing:.2em;text-transform:uppercase}
  .venue-name{margin-top:40px;font-family:"Playfair Display",serif;font-style:italic;font-weight:700;font-size:54px}
  .venue-address{margin-top:14px;font-family:"Comfortaa",sans-serif;font-weight:700;font-size:27px;letter-spacing:.2em;text-transform:uppercase;line-height:1.5}
</style>
</head>
<body>
<main class="canvas">
  <article class="label">
    <svg class="floral-art" viewBox="0 0 780 1060" role="img" aria-label="Watercolour anemone flower illustration in blush pink petals with a dark navy centre behind the couple's names">
      <defs>
        <radialGradient id="bloom" cx="390" cy="400" r="380" gradientUnits="userSpaceOnUse">
          <stop offset="0" stop-color="#262f42"/>
          <stop offset="0.2" stop-color="#262f42"/>
          <stop offset="0.29" stop-color="#a9b6c8"/>
          <stop offset="0.42" stop-color="#f2a9a3" stop-opacity="0.85"/>
          <stop offset="0.7" stop-color="#f7cfc8" stop-opacity="0.55"/>
          <stop offset="1" stop-color="#f7cfc8" stop-opacity="0"/>
        </radialGradient>
      </defs>
      <rect width="780" height="1060" fill="url(#bloom)"/>
    </svg>
    <div class="label-content">
      <p class="invite-line">You're cordially invited to the</p>
      <div class="rule"></div>
      <h1 class="event-title">Wedding of</h1>
      <div class="couple">
        <div class="partner"><span class="first-name">Clara</span><span class="surname">Whitmore</span></div>
        <span class="amp">&amp;</span>
        <div class="partner"><span class="first-name">Julian</span><span class="surname">Ashford</span></div>
      </div>
      <p class="details">On 24<sup>th</sup> of July 2018<br>Ceremony starts at 4</p>
      <p class="venue-heading">The Venue</p>
      <div class="rule short"></div>
      <p class="venue-name">The Grand Hall of Willows</p>
      <p class="venue-address">Heron Lane 4417<br>Fairhaven FL 32145</p>
    </div>
  </article>
</main>
</body>
</html>
```